Elegant Business Card with Logo and Picture

Please create a business card that has the Logo colors add Gold and turquoise / use the attached logo - I would like a beautiful Business Card - Please make sure it's printed on both sides / Picture can go on one side Logo other
www.velmorshine.example
614-372-0586
Lyn Odessa Ferwick
lynodessaf@quillpost.example
Life Coach
Vantrell Certified Teacher / Life Coach / Interior Designer
Transformational Retreats

Target Market(s)

Women Men General

Industry/Entity Type

Life Coaching

Contact Information for Business Card

www.velmorshine.example
614-372-0586
Lyn Odessa Ferwick
Life Coach
Vantrell Certified Teacher / Yoga Teacher / Interior Designer

Font styles to use
Serif
Decorative

Colors
33a6d6
e34197
ffc214

Requirements
Must have
• Quality Paper and touch /
Nice to have
• Beautiful Touch and feel
Should not have
• needs to be elegant

```html
<!DOCTYPE html>
<html lang="en">
<head>
<meta charset="utf-8">
<title>Velmor Shine Coaching — Business Card</title>
<link rel="stylesheet" href="https://fonts.googleapis.com/css2?family=Roboto+Slab:wght@400&family=Roboto:wght@500;700&family=Roboto+Condensed:wght@400;500&display=swap">
<style>
  :root {
    --stage: #1d1d1e;
    --ink: #0b0b0b;
    --card-black: #111112;
    --paper: #ffffff;
    --magenta: #ff0a7e;
    --muted: #3a3a3a;
  }
  * { box-sizing: border-box; margin: 0; padding: 0; }
  html, body { width: 1200px; height: 800px; overflow: hidden; background: var(--stage); }
  .canvas {
    position: relative; width: 1200px; height: 800px;
    display: flex; align-items: center; justify-content: center; gap: 40px;
  }
  .card {
    position: relative; width: 540px; height: 310px;
    border-radius: 18px; overflow: hidden;
  }

  /* Back side */
  .card--back { background: var(--card-black); }
  .back-mark {
    position: absolute; left: 50%; top: 52px; transform: translateX(-50%);
    width: 96px; height: 96px; border-radius: 50%;
    border: 4px solid var(--magenta);
    display: flex; align-items: center; justify-content: center;
    font-family: 'Roboto Slab', serif; font-size: 34px; color: var(--paper);
  }
  .back-brand {
    position: absolute; left: 0; right: 0; top: 172px; text-align: center;
    font-family: 'Roboto Slab', serif; color: var(--paper);
    font-size: 22px; letter-spacing: 4px;
  }
  .back-sub {
    position: absolute; left: 0; right: 0; top: 204px; text-align: center;
    font-family: 'Roboto Slab', serif; color: var(--magenta);
    font-size: 9px; letter-spacing: 12px; padding-left: 12px;
  }

  /* Front side */
  .card--front { background: var(--paper); }
  .pink-band {
    position: absolute; left: 330px; right: 0; top: 40px; height: 52px;
    background: var(--magenta);
  }
  .black-band {
    position: absolute; left: 0; top: 112px; width: 330px; height: 48px;
    background: var(--ink);
    clip-path: polygon(0 0, 100% 0, 93% 100%, 0 100%);
  }
  .band-brand {
    position: absolute; left: 60px; top: 120px; width: 210px; text-align: center;
    font-family: 'Roboto Slab', serif; color: var(--paper);
    font-size: 14px; letter-spacing: 2.5px;
  }
  .band-sub {
    position: absolute; left: 60px; top: 140px; width: 210px; text-align: center;
    font-family: 'Roboto Slab', serif; color: #cfcfcf;
    font-size: 6px; letter-spacing: 7px; padding-left: 7px;
  }
  .front-mark {
    position: absolute; left: 282px; top: 62px;
    width: 86px; height: 86px; border-radius: 50%;
    background: var(--paper); border: 4px solid var(--magenta);
    display: flex; align-items: center; justify-content: center;
    font-family: 'Roboto Slab', serif; font-size: 28px; color: var(--ink);
  }
  .portrait {
    position: absolute; left: 70px; top: 168px; width: 200px; height: 142px;
    border-radius: 90px 90px 0 0;
    background: linear-gradient(180deg, #d9b46e 0%, #e7a789 45%, #e69a8c 70%, #c95a78 100%);
  }
  .details { position: absolute; left: 300px; top: 176px; }
  .name {
    font-family: 'Roboto', sans-serif; font-weight: 700;
    color: var(--magenta); font-size: 17px; margin-bottom: 4px;
  }
  .roles {
    font-family: 'Roboto Condensed', sans-serif; font-weight: 500;
    color: var(--ink); font-size: 10.5px; line-height: 1.3; margin-bottom: 8px;
  }
  .contacts { list-style: none; }
  .contacts li {
    display: flex; align-items: center; gap: 6px;
    font-family: 'Roboto', sans-serif; font-weight: 500;
    color: var(--muted); font-size: 10px; line-height: 1.55;
  }
  .contacts svg { width: 9px; height: 9px; fill: var(--magenta); flex: none; }
</style>
</head>
<body>
<main class="canvas">

  <section class="card card--back" aria-label="Card back">
    <div class="back-mark">Lyn</div>
    <div class="back-brand">VELMOR SHINE</div>
    <div class="back-sub">COACHING</div>
  </section>

  <section class="card card--front" aria-label="Card front">
    <div class="pink-band"></div>
    <div class="black-band"></div>
    <div class="band-brand">VELMOR SHINE</div>
    <div class="band-sub">COACHING</div>
    <div class="front-mark">Lyn</div>

    <div class="portrait" role="img" aria-label="Portrait photo of the coach, smiling, in a striped off-shoulder top"></div>

    <div class="details">
      <p class="name">Lyn Odessa Ferwick</p>
      <p class="roles">Life Coach<br>Vantrell Certified Teacher /<br>Yoga Teacher / Interior Designer</p>
      <ul class="contacts">
        <li><svg viewBox="0 0 24 24" aria-hidden="true"><path d="M6.6 10.8a15.1 15.1 0 0 0 6.6 6.6l2.2-2.2c.3-.3.7-.4 1-.2 1.1.4 2.3.6 3.6.6.6 0 1 .4 1 1V20c0 .6-.4 1-1 1A17 17 0 0 1 3 4c0-.6.4-1 1-1h3.5c.6 0 1 .4 1 1 0 1.3.2 2.5.6 3.6.1.3 0 .7-.2 1z"/></svg>614-372-0586</li>
        <li><svg viewBox="0 0 24 24" aria-hidden="true"><path d="M2 5h20v14H2z M2 5l10 7 10-7" /></svg>lynodessaf@quillpost.example</li>
        <li><svg viewBox="0 0 24 24" aria-hidden="true"><circle cx="12" cy="12" r="10"/></svg>www.velmorshine.example</li>
      </ul>
    </div>
  </section>

</main>
</body>
</html>
```